Brovemo / stay-brightened -> Align your thoughts and emotions with world peace

[En español at the end] Very good! Thank you for showing interest in our project :) We need a logo design and web design for a foundation based in Barcelona. Our goal is to work with people's psychology and philosophy to make their lives happier as well as the rest of the world, because we believe we can align them. The name of the foundation is "brovemo" (brovémo), which comes to say that there is a way to align a series of concepts that take us from the peace and inner happiness of the individual to world peace and happiness. Very much in the line of Tomas Verlinde's quotation: "All the problems of humanity derive from that we do not know how to remain alone and quiet in a room". The concepts we want to align are the following, and in this order: Inner Peace Practical Philosophy Emotional Intelligence Critical Thinking Social Justice Conflict Resolution World Peace We enclose a couple of possible logo and web ideas, very grotesque and rudimentary. We are sure that you will be able to capture the idea and improve it in such a way that the idea will win with your contribution. Thank you very much in advance! Ah! And, brovemo :-) -------------- Hi! Thanks for paying attention to this project! We are looking for a logo and web design for an association whose goal is to work with the psychology and philosophy of people in order to make their life happier as well as the happiness of the rest of the world. The name of the organization is "brovemo" (get aligned) meaning that we can align ourselves with the next concepts (in this order): inner peace - practical philosophy - emotional intelligence - critical thinking - social justice - conflict resolution - global Peace Find some basic ideas that you might find in order to grasp what we are looking for, but feel free to add your own contribution, I am sure you can surprise us! :) Thank you in advance, Get aligned!

Target Market(s)

We addressed mainly middle-class people with concerns for personal development. In the medium term, we plan to cover the spectrum of companies with training courses for their staff. The first project that we are sure will be carried out is the application of critical thinking for adolescents and young people.

Logo Text

Brove-m

Number of Pages Required

1 page

Font styles to use
Sans Serif

Colors
3176b5
f37122

Requirements
Must have
• The essential elements are relatively abstract and numerous. Those exposed before: Inner Peace, Practical Philosophy, Emotional Intelligence, Critical Thinking, Social Justice, Conflict Resolution, World Peace. Probably the most striking or relevant will be two: emotional intelligence and critical thinking. The next level would be occupied by inner peace through meditation and introspection. And in the last level the other three.
Nice to have
• We want to transmit integrity and transparency, which in turn will be pillars of the educational and philosophical methods that we will teach. Empathy and compassion are also key. We have marked some colors, but still feel free to use another / others in your design. Sure you have great ideas :-) and we are looking forward to seeing them
Should not have
• We want to avoid at all costs the sensation of pseudoscience and volatility. Our values ​​are deep and we prefer to die rather than transmit an ambiguous, wrong, superfluous or interested message (in the sense of chaquetero).

```html
<!DOCTYPE html>
<html lang="es">
<head>
<meta charset="utf-8">
<title>brovemo – tu paz interior y la mundial</title>
<link href="https://fonts.googleapis.com/css2?family=Open+Sans:ital,wght@0,400;0,600;0,700;1,400&display=swap" rel="stylesheet">
<style>
:root{
  --brand-blue:#3176b5;
  --white:#ffffff;
  --nav-grey:#6c6c6c;
  --footer-bg:#1d1d1d;
  --footer-text:#8a8a8a;
  --rail:rgba(255,255,255,.55);
}
*{margin:0;padding:0;box-sizing:border-box}
html,body{width:1200px;height:4220px;overflow:hidden}
body{font-family:"Open Sans",Arial,sans-serif;background:var(--white);color:var(--white);position:relative}

.site-header{height:100px;background:var(--white);position:relative}
.brand{position:absolute;left:240px;top:22px;display:flex;align-items:center;gap:12px}
.brand-dot{width:56px;height:56px;border-radius:50%;background:var(--brand-blue)}
.brand-name{font-size:44px;font-weight:600;color:var(--brand-blue);letter-spacing:-.5px}
.main-nav{position:absolute;left:692px;top:42px;display:flex;gap:30px}
.main-nav a{font-size:13px;color:var(--nav-grey);text-decoration:none}

.hero{height:288px;position:relative;background:linear-gradient(100deg,#4a5560 0%,#6b7a84 30%,#8aa0ae 55%,#3e5b74 80%,#2b3f55 100%)}
.hero-title{position:absolute;top:8px;width:100%;text-align:center;font-size:31px;font-weight:700}
.hero-chain{position:absolute;left:0;top:0}

.stage{height:503px;position:relative;text-align:center}
.stage-inner{position:absolute;left:270px;width:660px;top:32px}
.stage h2{font-size:34px;font-weight:700;text-shadow:0 1px 3px rgba(0,0,0,.35)}
.stage .lead{font-size:11px;font-style:italic;line-height:1.35;margin:6px 10px 0}
.stage p.body{font-size:14px;font-style:italic;line-height:1.5;margin-top:40px;text-shadow:0 1px 2px rgba(0,0,0,.3)}
.stage p.body + p.body{margin-top:26px}
.stage-knot{position:absolute;left:969px;bottom:2px;width:20px;height:20px;border-radius:50%;border:1.5px solid var(--rail);background:rgba(255,255,255,.08)}
.rail{position:absolute;left:978px;top:388px;width:2px;height:3545px;background:var(--rail);z-index:2}

.stage--inner-peace{background:linear-gradient(180deg,#4d6d80,#6f8c8e 45%,#4f6a72)}
.stage--philosophy{background:linear-gradient(180deg,#5c4f43,#8a7764 50%,#4b3f35)}
.stage--emotion{background:linear-gradient(180deg,#b46f34,#c98a52 40%,#7a6a5e 75%,#4e4a4a)}
.stage--critical{background:linear-gradient(180deg,#3e3126,#6b5643 50%,#3a2e24)}
.stage--conflict{background:linear-gradient(180deg,#3a3f40,#565c5b 50%,#2e3233)}
.stage--justice{background:linear-gradient(180deg,#4fc7aa,#46b79b 60%,#399a82)}
.stage--world{background:linear-gradient(180deg,#3f7a2c,#5e9e3c 50%,#2f6a22)}

.site-footer{height:287px;background:var(--footer-bg);position:relative;text-align:center}
.footer-brand{position:absolute;left:0;width:100%;top:50px;display:flex;justify-content:center;align-items:center;gap:10px}
.footer-brand .brand-dot{width:46px;height:46px}
.footer-brand .brand-name{font-size:36px}
.footer-nav{position:absolute;top:132px;width:100%;display:flex;justify-content:center;gap:30px}
.footer-nav a{font-size:12px;color:var(--footer-text);text-decoration:none}
.social{position:absolute;top:196px;width:100%;display:flex;justify-content:center;gap:30px}
.social span{width:24px;height:24px;border-radius:50%;background:var(--brand-blue)}
.copyright{position:absolute;bottom:8px;width:100%;font-size:8px;color:#555}
</style>
</head>
<body>
<header class="site-header">
  <div class="brand"><span class="brand-dot"></span><span class="brand-name">brovemo</span></div>
  <nav class="main-nav"><a href="#">Inicio</a><a href="#">Nosotros</a><a href="#">participar</a><a href="#">contacto</a></nav>
</header>

<section class="hero" role="img" aria-label="Paisaje de montaña al atardecer con la cadena de conceptos">
  <h1 class="hero-title">brovemo-tu paz interior y la mundial</h1>
  <svg class="hero-chain" width="1200" height="288" viewBox="0 0 1200 288">
    <g fill="none" stroke="rgba(255,255,255,.5)" stroke-width="1.2" stroke-dasharray="3 4">
      <circle cx="340" cy="164" r="120"/>
      <circle cx="340" cy="164" r="160"/>
      <circle cx="340" cy="164" r="210"/>
    </g>
    <line x1="428" y1="160" x2="960" y2="158" stroke="rgba(255,255,255,.7)" stroke-width="1.5" stroke-dasharray="2 4"/>
    <circle cx="340" cy="164" r="98" fill="none" stroke="rgba(255,255,255,.6)" stroke-width="3"/>
    <circle cx="340" cy="164" r="88" fill="#fff"/>
    <text x="340" y="152" text-anchor="middle" font-family="Open Sans, sans-serif" font-size="34" font-weight="600" fill="#333">Paz</text>
    <text x="340" y="190" text-anchor="middle" font-family="Open Sans, sans-serif" font-size="34" font-weight="600" fill="#333">interior</text>
    <g font-family="Open Sans, sans-serif" font-size="11" font-weight="700" fill="#fff" text-anchor="middle">
      <circle cx="474" cy="158" r="31" fill="rgba(0,0,0,.25)" stroke="#fff" stroke-width="2"/>
      <text x="474" y="155">Filosofía</text><text x="474" y="169">Práctica</text>
      <circle cx="565" cy="158" r="31" fill="rgba(0,0,0,.25)" stroke="#fff" stroke-width="2"/>
      <text x="565" y="155">Inteligencia</text><text x="565" y="169">emocional</text>
      <circle cx="663" cy="158" r="31" fill="rgba(0,0,0,.25)" stroke="#fff" stroke-width="2"/>
      <text x="663" y="155">Pensamiento</text><text x="663" y="169">crítico</text>
      <circle cx="755" cy="158" r="31" fill="rgba(0,0,0,.25)" stroke="#fff" stroke-width="2"/>
      <text x="755" y="155">Resolución</text><text x="755" y="169">conflictos</text>
      <circle cx="838" cy="158" r="31" fill="rgba(0,0,0,.25)" stroke="#fff" stroke-width="2"/>
      <text x="838" y="155">Justicia</text><text x="838" y="169">social</text>
      <circle cx="933" cy="158" r="31" fill="rgba(0,0,0,.25)" stroke="#fff" stroke-width="2"/>
      <text x="933" y="155">Paz</text><text x="933" y="169">mundial</text>
    </g>
    <circle cx="979" cy="284" r="9" fill="none" stroke="#fff" stroke-width="1.5"/>
  </svg>
</section>

<div class="rail"></div>

<section class="stage stage--inner-peace" role="img" aria-label="Fotografía de un valle con río visto desde la montaña">
  <div class="stage-inner">
    <h2>Paz interior</h2>
    <p class="lead">Un breve texto de presentación que resume el sentido de esta etapa del camino y la une con la siguiente, paso a paso, con calma y claridad.</p>
    <p class="body">Trabajamos con la psicología y la filosofía de cada persona para que su vida sea más serena y feliz. Cada encuentro parte de la escucha atenta, del respeto y de la honestidad, y propone ejercicios sencillos que pueden practicarse en casa, en el aula o en el trabajo. Creemos que el bienestar propio y el de los demás avanzan juntos.</p>
    <p class="body">Nuestros talleres combinan reflexión, diálogo y práctica guiada. Los grupos son pequeños para que cada voz encuentre su espacio, y los materiales se comparten de forma abierta. Así construimos, entre todos, una base sólida de empatía, compasión y pensamiento claro que acompaña a cada participante mucho después de terminar el curso.</p>
  </div>
  <span class="stage-knot"></span>
</section>

<section class="stage stage--philosophy" role="img" aria-label="Fotografía de una figura pensativa entre libros en tonos sepia">
  <div class="stage-inner">
    <h2>Filosofía Práctica</h2>
    <p class="lead">Un breve texto de presentación que resume el sentido de esta etapa del camino y la une con la siguiente, paso a paso, con calma y claridad.</p>
    <p class="body">Trabajamos con la psicología y la filosofía de cada persona para que su vida sea más serena y feliz. Cada encuentro parte de la escucha atenta, del respeto y de la honestidad, y propone ejercicios sencillos que pueden practicarse en casa, en el aula o en el trabajo. Creemos que el bienestar propio y el de los demás avanzan juntos.</p>
    <p class="body">Nuestros talleres combinan reflexión, diálogo y práctica guiada. Los grupos son pequeños para que cada voz encuentre su espacio, y los materiales se comparten de forma abierta. Así construimos, entre todos, una base sólida de empatía, compasión y pensamiento claro que acompaña a cada participante mucho después de terminar el curso.</p>
  </div>
  <span class="stage-knot"></span>
</section>

<section class="stage stage--emotion" role="img" aria-label="Ilustración de un cerebro colorido sobre un paisaje montañoso">
  <div class="stage-inner">
    <h2>Inteligencia emocional</h2>
    <p class="lead">Un breve texto de presentación que resume el sentido de esta etapa del camino y la une con la siguiente, paso a paso, con calma y claridad.</p>
    <p class="body">Trabajamos con la psicología y la filosofía de cada persona para que su vida sea más serena y feliz. Cada encuentro parte de la escucha atenta, del respeto y de la honestidad, y propone ejercicios sencillos que pueden practicarse en casa, en el aula o en el trabajo. Creemos que el bienestar propio y el de los demás avanzan juntos.</p>
    <p class="body">Nuestros talleres combinan reflexión, diálogo y práctica guiada. Los grupos son pequeños para que cada voz encuentre su espacio, y los materiales se comparten de forma abierta. Así construimos, entre todos, una base sólida de empatía, compasión y pensamiento claro que acompaña a cada participante mucho después de terminar el curso.</p>
  </div>
  <span class="stage-knot"></span>
</section>

<section class="stage stage--critical" role="img" aria-label="Fotografía de un laberinto circular visto desde arriba">
  <div class="stage-inner">
    <h2>Pensamiento crítico</h2>
    <p class="lead">Un breve texto de presentación que resume el sentido de esta etapa del camino y la une con la siguiente, paso a paso, con calma y claridad.</p>
    <p class="body">Trabajamos con la psicología y la filosofía de cada persona para que su vida sea más serena y feliz. Cada encuentro parte de la escucha atenta, del respeto y de la honestidad, y propone ejercicios sencillos que pueden practicarse en casa, en el aula o en el trabajo. Creemos que el bienestar propio y el de los demás avanzan juntos.</p>
    <p class="body">Nuestros talleres combinan reflexión, diálogo y práctica guiada. Los grupos son pequeños para que cada voz encuentre su espacio, y los materiales se comparten de forma abierta. Así construimos, entre todos, una base sólida de empatía, compasión y pensamiento claro que acompaña a cada participante mucho después de terminar el curso.</p>
  </div>
  <span class="stage-knot"></span>
</section>

<section class="stage stage--conflict" role="img" aria-label="Fotografía de un apretón de manos en tonos oscuros">
  <div class="stage-inner">
    <h2>Resolución conflictos</h2>
    <p class="lead">Un breve texto de presentación que resume el sentido de esta etapa del camino y la une con la siguiente, paso a paso, con calma y claridad.</p>
    <p class="body">Trabajamos con la psicología y la filosofía de cada persona para que su vida sea más serena y feliz. Cada encuentro parte de la escucha atenta, del respeto y de la honestidad, y propone ejercicios sencillos que pueden practicarse en casa, en el aula o en el trabajo. Creemos que el bienestar propio y el de los demás avanzan juntos.</p>
    <p class="body">Nuestros talleres combinan reflexión, diálogo y práctica guiada. Los grupos son pequeños para que cada voz encuentre su espacio, y los materiales se comparten de forma abierta. Así construimos, entre todos, una base sólida de empatía, compasión y pensamiento claro que acompaña a cada participante mucho después de terminar el curso.</p>
  </div>
  <span class="stage-knot"></span>
</section>

<section class="stage stage--justice" role="img" aria-label="Fotografía de muchas manos alzadas sobre fondo turquesa">
  <div class="stage-inner">
    <h2>Justicia social</h2>
    <p class="lead">Un breve texto de presentación que resume el sentido de esta etapa del camino y la une con la siguiente, paso a paso, con calma y claridad.</p>
    <p class="body">Trabajamos con la psicología y la filosofía de cada persona para que su vida sea más serena y feliz. Cada encuentro parte de la escucha atenta, del respeto y de la honestidad, y propone ejercicios sencillos que pueden practicarse en casa, en el aula o en el trabajo. Creemos que el bienestar propio y el de los demás avanzan juntos.</p>
    <p class="body">Nuestros talleres combinan reflexión, diálogo y práctica guiada. Los grupos son pequeños para que cada voz encuentre su espacio, y los materiales se comparten de forma abierta. Así construimos, entre todos, una base sólida de empatía, compasión y pensamiento claro que acompaña a cada participante mucho después de terminar el curso.</p>
  </div>
  <span class="stage-knot"></span>
</section>

<section class="stage stage--world" role="img" aria-label="Fotografía de manos sosteniendo el planeta entre hojas verdes">
  <div class="stage-inner">
    <h2>Paz mundial</h2>
    <p class="lead">Un breve texto de presentación que resume el sentido de esta etapa del camino y la une con la siguiente, paso a paso, con calma y claridad.</p>
    <p class="body">Trabajamos con la psicología y la filosofía de cada persona para que su vida sea más serena y feliz. Cada encuentro parte de la escucha atenta, del respeto y de la honestidad, y propone ejercicios sencillos que pueden practicarse en casa, en el aula o en el trabajo. Creemos que el bienestar propio y el de los demás avanzan juntos.</p>
    <p class="body">Nuestros talleres combinan reflexión, diálogo y práctica guiada. Los grupos son pequeños para que cada voz encuentre su espacio, y los materiales se comparten de forma abierta. Así construimos, entre todos, una base sólida de empatía, compasión y pensamiento claro que acompaña a cada participante mucho después de terminar el curso.</p>
  </div>
  <span class="stage-knot"></span>
</section>

<footer class="site-footer">
  <div class="footer-brand"><span class="brand-dot"></span><span class="brand-name">brovemo</span></div>
  <nav class="footer-nav"><a href="#">Inicio</a><a href="#">Nosotros</a><a href="#">participar</a><a href="#">contacto</a></nav>
  <div class="social" aria-label="Redes sociales"><span></span><span></span><span></span><span></span><span></span><span></span></div>
  <p class="copyright">Todos los derechos reservados</p>
</footer>
</body>
</html>
```